Marrowind Vodka logo and label design

We would like a logo and bottle label design for a new line of Ultra-Premium Vodka. The Company is called Marrowind Spirits and is based in Brisbane, Australia. We would like a 'Gatsby/Prohibition era vibe to the design. We want to keep it minimalistic and sleek. We strongly prefer a minimalist design and colour palette. Black,Gold,Grey,White,Silver,Red and Blue

The bottle will be similar in shape to Halvorak/Pale Heron. There will also need to be space on the label for required information, as well as short bio of the company, which will be provided to the winning design.

We would like to add the polish code of arms for Opoczno. Have attached link for reference. https://www.crestarchive-demo.net/crestarchive/index.php?title=Opoczno

Target Market(s)

Luxury brand customers

Logo Text

Marrowind Ultra-Premium Vodka

Logo styles of interest
Wordmark Logo
Lettermark Logo
Requirements
Must have
• This is the first release from our new Vodka label. We want a logo and bottle label that reflects a premium product. We very much like Prohibition/Gatsby era themed bottles and labels. The label and bottle should be elegant and clean.
Should not have
• Anything too busy or confusing.

```html
<!DOCTYPE html>
<html lang="en">
<head>
<meta charset="utf-8">
<title>Marrowind Ultra-Premium Vodka — Label</title>
<link rel="stylesheet" href="https://fonts.googleapis.com/css2?family=Marcellus&family=Josefin+Sans:wght@600&display=swap">
<style>
  :root {
    --backdrop: #1c1c1c;
    --label-black: #030303;
    --gold: #c9a24a;
    --gold-deep: #b07a2a;
  }
  html, body {
    margin: 0;
    padding: 0;
    width: 1200px;
    height: 2548px;
    overflow: hidden;
    background: var(--backdrop);
  }
  .canvas {
    position: relative;
    width: 1200px;
    height: 2548px;
  }
  .label {
    position: absolute;
    left: 150px;
    top: 580px;
    width: 900px;
    height: 1387px;
  }
  .label-body { fill: var(--label-black); }
  .label-edge { fill: none; stroke: var(--gold-deep); stroke-width: 5; }
  .label-top-rule { stroke: var(--gold); stroke-width: 6; }
  .brand-name {
    font-family: 'Marcellus', serif;
    fill: var(--gold);
    font-size: 104px;
    letter-spacing: 2px;
  }
  .tagline {
    font-family: 'Josefin Sans', sans-serif;
    font-weight: 600;
    fill: var(--gold);
    font-size: 30px;
    letter-spacing: 7px;
  }
</style>
</head>
<body>
<main class="canvas">
  <svg class="label" viewBox="0 0 900 1387" role="img" aria-label="Marrowind Ultra-Premium Vodka bottle label">
    <path class="label-body" d="M0,0 H900 V946 C900,1200 700,1387 450,1387 C200,1387 0,1200 0,946 Z"/>
    <path class="label-edge" d="M4,4 H896 V946 C896,1196 698,1383 450,1383 C202,1383 4,1196 4,946 Z"/>
    <line class="label-top-rule" x1="0" y1="6" x2="900" y2="6"/>
    <text class="brand-name" x="450" y="622" text-anchor="middle">MARROWIND</text>
    <text class="tagline" x="450" y="690" text-anchor="middle">ULTRA-PREMIUM VODKA</text>
  </svg>
</main>
</body>
</html>
```